Silver Creek Plumbing Business card & letter head design

We need a new business card and letter head for our plumbing company called silver creek plumbing. attached is the companys logo. We provide domestic and commercial plumbing services in regional western Australia. We are after Something simple yet nice to look at and something that fits within the trade industry.

Target Market(s)

trade/building industry

Contact Information for Business Card

Darl Hensby
Manager
0461 238 574
enquiries@scplumbwork.net.au
ABN: 47 381 905 462
PCL: 5187

Domestic & Commercial Plumbing
Tip Truck & Excavator hire

Colors

Designer to choose colors to be used in the design.

```html
<!DOCTYPE html>
<html lang="en">
<head>
<meta charset="utf-8">
<title>Silver Creek Plumbing – Letterhead</title>
<link rel="stylesheet" href="https://fonts.googleapis.com/css2?family=Open+Sans:wght@400;600;700&display=swap">
<style>
  :root {
    --brand-blue: #0d5aa7;
    --band-grey: #5a5a5a;
    --ink: #2b2b2b;
    --muted: #555555;
    --stage: #e6e7e9;
    --paper: #ffffff;
  }
  * { box-sizing: border-box; margin: 0; padding: 0; }
  html, body { width: 1200px; height: 1200px; overflow: hidden; }
  body {
    background: var(--stage);
    font-family: "Open Sans", Arial, sans-serif;
    color: var(--ink);
    position: relative;
  }
  .letterhead {
    position: absolute;
    left: 193px; top: 30px;
    width: 814px; height: 1140px;
    background: var(--paper);
    box-shadow: 0 4px 16px rgba(0,0,0,.15);
  }
  .side-bar { position: absolute; left: 0; width: 32px; background: var(--brand-blue); }
  .side-bar--top { top: 0; height: 1052px; }
  .side-bar--bottom { top: 1092px; height: 48px; }

  .brand {
    position: absolute; left: 106px; top: 82px;
    display: flex; align-items: center; gap: 8px;
    color: var(--brand-blue); font-weight: 700; font-size: 19px;
    letter-spacing: .2px; white-space: nowrap;
  }
  .brand-dot { width: 14px; height: 14px; border-radius: 50%; background: var(--brand-blue); }

  .recipient { position: absolute; left: 106px; top: 244px; font-size: 13px; line-height: 19px; }
  .salutation { position: absolute; left: 106px; top: 360px; font-size: 13px; }
  .letter-body p {
    position: absolute; left: 106px; width: 610px;
    font-size: 12.6px; line-height: 25.4px; color: #333;
  }
  .p1 { top: 399px; } .p2 { top: 501px; } .p3 { top: 603px; } .p4 { top: 705px; }

  .signature-mark {
    position: absolute; left: 104px; top: 850px; width: 112px; height: 34px;
    background: linear-gradient(90deg, #ececec, #f6f6f6);
    border-radius: 4px;
  }
  .signatory { position: absolute; left: 105px; top: 888px; font-size: 13px; line-height: 15px; }
  .signatory strong { font-weight: 700; display: block; }
  .signatory span { color: var(--muted); }

  .footer-band { position: absolute; left: 0; top: 1052px; width: 814px; height: 40px; }
  .footer-band::before { content: ""; position: absolute; left: 0; top: 0; width: 32px; height: 40px; background: var(--band-grey); }
  .footer-band::after { content: ""; position: absolute; right: 0; top: 0; width: 32px; height: 40px; background: var(--band-grey); }
  .footer-address { position: absolute; left: 107px; top: 8px; font-size: 9.4px; line-height: 16px; color: var(--muted); }
  .footer-divider { position: absolute; left: 261px; top: 0; width: 1px; height: 40px; background: #999; }
  .footer-contacts { position: absolute; left: 281px; top: 5px; font-size: 9.4px; line-height: 17px; color: var(--muted); }
  .footer-contacts .row { display: flex; align-items: center; gap: 6px; white-space: nowrap; }
  .footer-contacts .gap { width: 12px; }
  .footer-contacts svg { width: 11px; height: 11px; fill: var(--brand-blue); }
  .reg { color: var(--brand-blue); font-weight: 600; }
  .web-tab {
    position: absolute; left: 659px; top: 0; width: 125px; height: 40px;
    background: var(--brand-blue); color: #fff; font-size: 9.6px;
    display: flex; align-items: center; justify-content: center; gap: 5px;
  }
  .web-tab svg { width: 10px; height: 10px; }
</style>
</head>
<body>
<main class="letterhead">
  <div class="side-bar side-bar--top"></div>
  <div class="side-bar side-bar--bottom"></div>

  <div class="brand"><span class="brand-dot"></span>Silver Creek Plumbing</div>

  <address class="recipient" style="font-style:normal">
    Mr/s<br>First &amp; Last name<br>Company Name<br>Address
  </address>

  <p class="salutation">Dear Sir</p>

  <section class="letter-body">
    <p class="p1">This is a sample letter that has been placed to demonstrate typing remat (Your Company). letterhead design. When positioned properly, it will serve to work in harmony with all other elements letterhead. This letterhead design is meant to project an image</p>
    <p class="p2">This letterhead design is meant project an image of professionalism reliability. By using simple aligen we have created a very spacious feeling. The simplicity suggest rengththe spaciousnes contributes h aesthetics the layout. These basic qualities along with te (Your Company)</p>
    <p class="p3">look and helps reinforce the (Your Company) brand. letterhead design is meant to project an image p design. When positioned properly, it will serve to work in harmony all the other elements letterhead. sionalism and reliability.</p>
    <p class="p4">This letterhead design is based on the (Form of your logo) form (Your Company) logo. Each stationery we have created a very spacious feeling. The simplicity suggests strength the spaciousnes contribute part of the (Form of your logo).</p>
  </section>

  <div class="signature-mark" role="img" aria-label="Handwritten signature of Darl Hensby"></div>
  <div class="signatory"><strong>Darl Hensby</strong><span>Manager</span></div>

  <footer class="footer-band">
    <div class="footer-address">42 Harbour Road Albany,<br>WA 6330</div>
    <div class="footer-divider"></div>
    <div class="footer-contacts">
      <div class="row">
        <svg viewBox="0 0 24 24"><path d="M6.6 10.8a15.1 15.1 0 0 0 6.6 6.6l2.2-2.2a1 1 0 0 1 1-.25 11.4 11.4 0 0 0 3.6.57 1 1 0 0 1 1 1V20a1 1 0 0 1-1 1A17 17 0 0 1 3 4a1 1 0 0 1 1-1h3.5a1 1 0 0 1 1 1c0 1.25.2 2.45.57 3.57a1 1 0 0 1-.25 1z"/></svg>
        <span>0461 238 574</span><span class="gap"></span>
        <svg viewBox="0 0 24 24"><path d="M2 5h20v14H2z M2 5l10 8 10-8" fill="var(--brand-blue)"/><path d="M2 6l10 7 10-7" fill="none" stroke="#fff" stroke-width="1.6"/></svg>
        <span>enquiries@scplumbwork.net.au</span>
      </div>
      <div class="row"><span class="reg">ABN: 47 381 905 462 &nbsp;&nbsp;| &nbsp;&nbsp;PCL: 5187</span></div>
    </div>
    <div class="web-tab">
      <svg viewBox="0 0 24 24" fill="none" stroke="#fff" stroke-width="2"><circle cx="12" cy="12" r="10"/><path d="M2 12h20M12 2a15 15 0 0 1 0 20M12 2a15 15 0 0 0 0 20"/></svg>
      <span>scplumbwork.net.au</span>
    </div>
  </footer>
</main>
</body>
</html>
```